organic, healthy living website needs a new home page!

We need a home page for the front page of our website (www.saffronmeadowlark.com.au).

We want to see the following at a glance! We want to gain trust - communicate value, and navigate visitors to the next step - purchasing!

Our two main products:
- certified organic veggies (weekly in Melbourne, Australia - Mentone, Frankston and Ringwood with more pick up locations to come soon)

-ethical wooden toys (by membership only at this stage - run quarterly as a bulk buy - just for Melbourne people!)

Other products:
- health appliances - juicers, dehydrators and water filters (free delivery to their door all over Australia)

- natural parenting products which promote breastfeeding, homebirth, cosleeping and gentle parenting (books, jewellery, gifts, blessingway etc) all over Australia - send via Koala Parcel.

This website holds all of our products for purchase. We want to emphasise exactly what is to offer here. We will have an info blog which we want to link THROUGH the product homepage of SM. The blog will include a directory of natural services (for a very niche market), recipes, stories, and a wealth of information to do with natural pregnancy, health, parenting, health and community!

We have 5 images linked below - we need these to correspond with the words PREGNANCY, BIRTH, PARENTING, HEALTH, And COMMUNITY and maybe a little design on these - such as dragonflies or flowers - or both. We will code these to work in a slideshow, and link to our blog.

We want this page to feature everything we do, but also be aesthetically pleasing without overkill. We want it to reflect our style, and vision. Natural, organic, and as close to nature as possible. Flow is important, as is consistency throughout the page. WE want it to appeal to our hippy mamas and papas who just want to love their babies, live organically and as healthy as they can.

We love the look and feel of the following websites:

http://thebrightlarderapp.com/

Thank you!!
Updates

Target Market(s)

20-50 year old parents who are environmentally aware and health conscious. They have very close bonds to their children.
Think bohemian, rustic, vintage yet with a modern feel.

Industry/Entity Type

Health

Font styles to use
Script

Colors
e34197
6b449b
33a6d7
0455a3
33b7a4

Requirements
Must have
• Must be clean and say at a glance exactly what we do.

```html
<!DOCTYPE html>
<html lang="en">
<head>
<meta charset="utf-8">
<title>SaffronMeadowlark – Organic Healthy Living</title>
<link rel="stylesheet" href="https://fonts.googleapis.com/css2?family=Great+Vibes&family=Pinyon+Script&family=Merriweather+Sans:ital,wght@0,400;0,700;1,400;1,700;1,800&family=Roboto+Condensed:wght@400;700&family=Playfair+Display:wght@700&family=Open+Sans:wght@400;600&display=swap">
<style>
  :root{
    --ink:#231f20;
    --pink:#e34197;
    --pink-soft:#d9489c;
    --pink-deep:#c8337f;
    --purple:#6b449b;
    --sky:#33a6d7;
    --navy:#0455a3;
    --teal:#33b7a4;
    --paper:#ffffff;
    --mist:#eeeeee;
    --rule:#d6d6d6;
    --lavender:#e4e0ee;
  }
  *{box-sizing:border-box;margin:0;padding:0}
  html,body{width:1200px;height:2267px;overflow:hidden}
  body{position:relative;background:var(--paper);color:var(--ink);font-family:"Open Sans",sans-serif}
  a{color:inherit;text-decoration:none}

  /* utility bar */
  .utility-bar{position:absolute;left:0;top:0;width:1200px;height:45px;background:var(--ink);color:#fff;font-size:12px}
  .utility-links{position:absolute;left:155px;top:14px;display:flex;gap:20px}
  .utility-links a{display:flex;align-items:center;gap:5px}
  .utility-links svg{width:11px;height:11px;fill:var(--teal)}
  .account-links{position:absolute;left:717px;top:14px;display:flex;gap:12px}
  .account-links span{border-left:1px solid #fff;height:18px;margin-top:-2px}
  .search{position:absolute;left:842px;top:5px;display:flex}
  .search-field{width:155px;height:32px;background:var(--lavender);padding:0 6px;font-size:13px;color:#fff;text-transform:uppercase;display:flex;align-items:center}
  .search-button{width:37px;height:32px;background:var(--teal);margin-left:2px;display:flex;align-items:center;justify-content:center}

  /* hero */
  .hero{position:absolute;left:0;top:45px;width:1200px;height:620px;overflow:hidden}
  .hero-photo{position:absolute;inset:0;background:
      radial-gradient(ellipse 170px 150px at 900px 270px,#e0452c 0%,#c8361f 55%,transparent 100%),
      radial-gradient(ellipse 150px 140px at 1060px 230px,#d8472a 0%,#b52e1c 55%,transparent 100%),
      radial-gradient(ellipse 160px 130px at 990px 400px,#b8261a 0%,#92251a 55%,transparent 100%),
      radial-gradient(ellipse 140px 110px at 1160px 360px,#c63a22 0%,transparent 100%),
      radial-gradient(ellipse 420px 220px at 900px 520px,#8a4b26 0%,#6e3a1e 50%,transparent 100%),
      radial-gradient(ellipse 160px 70px at 260px 590px,#d55a34 0%,transparent 100%),
      radial-gradient(ellipse 150px 70px at 520px 595px,#e6c96a 0%,transparent 100%),
      radial-gradient(ellipse 520px 360px at 280px 170px,#fbf7a6 0%,#f1ea6c 40%,transparent 85%),
      radial-gradient(ellipse 600px 200px at 250px 560px,#8fae2c 0%,#a8c23c 50%,transparent 100%),
      linear-gradient(90deg,#b9cf3e 0%,#ece36e 38%,#e2c65a 58%,#b87a3a 80%,#8a4a22 100%)}
  .edge-top,.edge-bottom{position:absolute;left:0;width:1200px;height:10px;background-size:12px 10px;background-repeat:repeat-x}
  .edge-top{top:0;background-image:linear-gradient(135deg,var(--ink) 50%,transparent 51%),linear-gradient(-135deg,var(--ink) 50%,transparent 51%)}
  .edge-bottom{bottom:0;background-image:linear-gradient(45deg,var(--ink) 50%,transparent 51%),linear-gradient(-45deg,var(--ink) 50%,transparent 51%)}
  .brand{position:absolute;left:170px;top:22px;display:flex;align-items:center;gap:10px;font-family:"Merriweather Sans",sans-serif;font-weight:400;font-size:24px;color:var(--navy)}
  .brand-mark{width:40px;height:40px;border-radius:50%;background:var(--purple)}
  .main-nav{position:absolute;left:643px;top:23px;display:flex;align-items:center;font-size:12px;text-transform:uppercase}
  .main-nav a{padding:0 14px;height:35px;line-height:35px;margin-right:12px}
  .main-nav .is-active{background:var(--sky);color:#fff}
  .hero-script{position:absolute;left:184px;top:178px;font-family:"Great Vibes",cursive;font-weight:400;font-size:112px;color:var(--pink-soft);line-height:1}
  .hero-tagline{position:absolute;left:186px;top:336px;font-family:"Merriweather Sans",sans-serif;font-style:italic;font-weight:800;font-size:39px;line-height:49px;color:var(--ink)}
  .shop-now{position:absolute;left:810px;top:494px;width:189px;height:41px;background:var(--ink);color:#fff;font-family:"Merriweather Sans",sans-serif;font-style:italic;font-weight:800;font-size:21px;display:flex;align-items:center;justify-content:center;border-left:12px solid var(--teal);border-right:12px solid var(--teal)}

  /* section headings */
  .section-title{position:absolute;left:0;width:1200px;text-align:center;font-family:"Pinyon Script",cursive;font-weight:400;font-size:42px;color:var(--ink);line-height:1}
  .divider{position:absolute;height:1px;background:var(--rule)}

  /* product cards */
  .deal-cards{position:absolute;left:175px;top:759px;display:flex;gap:10px}
  .deal-card{width:204px;height:274px;background:var(--ink);color:#fff;text-align:center}
  .deal-image{height:151px}
  .deal-image.red{background:radial-gradient(ellipse 34px 62px at 50% 52%,#b3161e 0%,#8e1218 60%,transparent 100%),var(--mist)}
  .deal-image.steel{background:radial-gradient(ellipse 34px 62px at 50% 52%,#d9d9d9 0%,#8f8f8f 60%,transparent 100%),var(--mist)}
  .deal-label{height:24px;line-height:24px;background:var(--sky);font-family:"Pinyon Script",cursive;font-size:18px}
  .deal-price{margin-top:10px;font-family:"Playfair Display",serif;font-weight:700;font-size:32px;line-height:1}
  .deal-stars{margin-top:6px;font-size:11px;letter-spacing:1px}
  .deal-stars .off{color:var(--sky)}
  .deal-button{display:inline-block;margin-top:6px;background:#fff;color:var(--ink);font-size:9px;padding:2px 7px;text-transform:uppercase;border-radius:2px}

  /* blog grid */
  .post{position:absolute;width:281px}
  .post-image{height:156px}
  .post-head{position:relative;margin-top:14px}
  .post-title{font-family:"Roboto Condensed",sans-serif;font-size:15px;color:var(--pink)}
  .post-date{font-family:"Roboto Condensed",sans-serif;font-size:10px;margin-top:4px}
  .post-comments{position:absolute;right:0;top:-2px;text-align:right;font-family:"Roboto Condensed",sans-serif;font-size:10px}
  .post-comments svg{display:block;margin:0 6px 2px auto}
  .post-body{margin-top:14px;font-family:"Merriweather Sans",sans-serif;font-style:italic;font-weight:700;font-size:11.5px;line-height:19px;text-align:justify}
  .post-more{margin-top:14px;text-align:right;font-family:"Merriweather Sans",sans-serif;font-style:italic;font-size:10px;color:var(--pink-deep)}

  /* testimonial */
  .avatar{position:absolute;left:555px;top:1950px;width:90px;height:90px;border-radius:50%;background:radial-gradient(circle at 50% 45%,#e8d2bd 0%,#c9a98c 55%,#8c7a6a 100%);border:5px solid var(--ink);box-shadow:0 0 0 3px #fff,0 0 0 4px #999}
  .quote-mark{position:absolute;font-family:"Playfair Display",serif;font-weight:700;font-size:56px;color:var(--sky);line-height:1}
  .quote-text{position:absolute;left:267px;top:2066px;width:670px;font-family:"Merriweather Sans",sans-serif;font-style:italic;font-size:11px;line-height:19px;color:#333}
  .quote-name{position:absolute;left:0;top:2122px;width:1200px;text-align:center;font-family:"Merriweather Sans",sans-serif;font-style:italic;font-weight:700;font-size:14px;color:var(--pink-deep)}

  /* footer */
  .footer-band{position:absolute;left:0;top:2153px;width:1200px;height:10px;background:var(--pink)}
  .site-footer{position:absolute;left:0;top:2163px;width:1200px;height:104px;background:var(--ink);color:#fff;text-align:center}
  .footer-note{margin-top:14px;font-family:"Merriweather Sans",sans-serif;font-size:12px}
  .social{display:flex;justify-content:center;gap:2px;margin-top:12px}
  .social span{width:46px;height:46px;border-radius:50%}
  .social .one{background:#3c5a98}
  .social .two{background:#c9453a}
  .social .three{background:#2fa7df}
</style>
</head>
<body>

<header class="utility-bar">
  <nav class="utility-links">
    <a href="#"><svg viewBox="0 0 10 10"><path d="M5 0 0 5h1.5v5h2.5V7h2v3h2.5V5H10z"/></svg>Home</a>
    <a href="#"><svg viewBox="0 0 10 10"><circle cx="5" cy="3" r="2.5"/><path d="M0 10c0-3 2-4.5 5-4.5s5 1.5 5 4.5z"/></svg>My Account</a>
    <a href="#"><svg viewBox="0 0 10 10"><path d="M0 1h2l1.5 5h5L10 2.5H3" stroke="#33b7a4" fill="none"/><circle cx="4" cy="8.5" r="1"/><circle cx="8" cy="8.5" r="1"/></svg>My Cart</a>
    <a href="#"><svg viewBox="0 0 10 10"><path d="M5 9 1 5a2.3 2.3 0 0 1 4-3 2.3 2.3 0 0 1 4 3z"/></svg>Wish List</a>
  </nav>
  <div class="account-links"><a href="#">Register</a><span></span><a href="#">Login</a></div>
  <div class="search">
    <div class="search-field">Search</div>
    <div class="search-button"><svg width="20" height="20" viewBox="0 0 20 20"><circle cx="8" cy="8" r="5.5" stroke="#fff" stroke-width="2.5" fill="none"/><path d="M12 12l6 6" stroke="#fff" stroke-width="3"/></svg></div>
  </div>
</header>

<section class="hero">
  <div class="hero-photo" role="img" aria-label="Wicker basket full of fresh red organic apples in sunlit green grass"></div>
  <div class="edge-top"></div>
  <div class="brand"><span class="brand-mark"></span>SaffronMeadowlark</div>
  <nav class="main-nav">
    <a href="#" class="is-active">Health Appliances</a>
    <a href="#">Natural Parenting</a>
    <a href="#">Blog</a>
  </nav>
  <h1 class="hero-script">Lorem ipsum</h1>
  <p class="hero-tagline">Lorem ipsum dolor sit amet,<br>consectetur adipisicing elit</p>
  <a href="#" class="shop-now">SHOP NOW</a>
  <div class="edge-bottom"></div>
</section>

<h2 class="section-title" style="top:690px">Hot Deal</h2>
<div class="deal-cards">
  <article class="deal-card">
    <div class="deal-image red" role="img" aria-label="Red slow juicer"></div>
    <div class="deal-label">Sed Ut Perspiciatis</div>
    <div class="deal-price">$550</div>
    <div class="deal-stars">★★★★<span class="off">★</span></div>
    <a href="#" class="deal-button">Shop Now</a>
  </article>
  <article class="deal-card">
    <div class="deal-image steel" role="img" aria-label="Stainless steel slow juicer"></div>
    <div class="deal-label">Sed Ut Perspiciatis</div>
    <div class="deal-price">$550</div>
    <div class="deal-stars">★★★★<span class="off">★</span></div>
    <a href="#" class="deal-button">Shop Now</a>
  </article>
  <article class="deal-card">
    <div class="deal-image steel" role="img" aria-label="Stainless steel slow juicer"></div>
    <div class="deal-label">Sed Ut Perspiciatis</div>
    <div class="deal-price">$550</div>
    <div class="deal-stars">★★★<span class="off">★★</span></div>
    <a href="#" class="deal-button">Shop Now</a>
  </article>
  <article class="deal-card">
    <div class="deal-image steel" role="img" aria-label="Stainless steel slow juicer"></div>
    <div class="deal-label">Sed Ut Perspiciatis</div>
    <div class="deal-price">$550</div>
    <div class="deal-stars">★★★★<span class="off">★</span></div>
    <a href="#" class="deal-button">Shop Now</a>
  </article>
</div>

<div class="divider" style="left:150px;top:1085px;width:894px"></div>
<h2 class="section-title" style="top:1115px">Hot Deal</h2>

<article class="post" style="left:150px;top:1193px">
  <div class="post-image" role="img" aria-label="Community: many hands in a circle around a smiley face drawn in white sand" style="background:radial-gradient(ellipse 90px 60px at 50% 50%,#f6f3ee 0%,#ebe5dd 60%,transparent 100%),radial-gradient(ellipse 160px 90px at 50% 50%,transparent 55%,#d8b8a0 80%,transparent 100%),linear-gradient(135deg,#e7dfd6,#d2c4b6)"></div>
  <div class="post-head"><div class="post-title">Lorem ipsum dolor</div><div class="post-date">Jan 2014</div>
    <div class="post-comments"><svg width="26" height="12" viewBox="0 0 26 12"><path d="M4 1h18c3 0 4 2 3 5s-4 4-8 4H9L2 12l2-3C0 8 0 1 4 1z" fill="#231f20"/></svg>Comments</div></div>
  <p class="post-body">Lorem ipsum dolor sit amet, consectetur adipisicing elit, sed do eiusmod tempor incididunt ut labore et dolore magna aliqua.</p>
  <div class="post-more">Read more</div>
</article>
<article class="post" style="left:458px;top:1193px">
  <div class="post-image" role="img" aria-label="Health: halved green kiwi fruit on a wooden board" style="background:radial-gradient(ellipse 60px 70px at 25% 50%,#e9eccf 0%,#9fc13a 25%,#6f9a22 70%,transparent 100%),radial-gradient(ellipse 75px 55px at 72% 38%,#eef0d6 0%,#a8c640 25%,#76a026 70%,transparent 100%),linear-gradient(135deg,#a07452,#8b6247 60%,#7a5540)"></div>
  <div class="post-head"><div class="post-title">Lorem ipsum dolor</div><div class="post-date">Jan 2014</div>
    <div class="post-comments"><svg width="26" height="12" viewBox="0 0 26 12"><path d="M4 1h18c3 0 4 2 3 5s-4 4-8 4H9L2 12l2-3C0 8 0 1 4 1z" fill="#231f20"/></svg>Comments</div></div>
  <p class="post-body">Lorem ipsum dolor sit amet, consectetur adipisicing elit, sed do eiusmod tempor incididunt ut labore et dolore magna aliqua.</p>
  <div class="post-more">Read more</div>
</article>
<article class="post" style="left:769px;top:1193px">
  <div class="post-image" role="img" aria-label="Pregnancy: hands cradling a pregnant belly, wearing a turquoise beaded bracelet" style="background:radial-gradient(ellipse 110px 70px at 40% 60%,#e2b59c 0%,#d4a085 60%,transparent 100%),radial-gradient(ellipse 20px 30px at 76% 50%,#2ab0b4 0%,transparent 100%),linear-gradient(135deg,#f2ebe6,#e6cfc2 60%,#cfae9c)"></div>
  <div class="post-head"><div class="post-title">Lorem ipsum dolor</div><div class="post-date">Jan 2014</div>
    <div class="post-comments"><svg width="26" height="12" viewBox="0 0 26 12"><path d="M4 1h18c3 0 4 2 3 5s-4 4-8 4H9L2 12l2-3C0 8 0 1 4 1z" fill="#231f20"/></svg>Comments</div></div>
  <p class="post-body">Lorem ipsum dolor sit amet, consectetur adipisicing elit, sed do eiusmod tempor incididunt ut labore et dolore magna aliqua.</p>
  <div class="post-more">Read more</div>
</article>

<article class="post" style="left:150px;top:1533px">
  <div class="post-image" role="img" aria-label="Parenting: a family walking hand in hand along a beach at sunset" style="background:linear-gradient(180deg,#f3c99a 0%,#e9b385 30%,#c99a78 42%,#e0a676 55%,#d39467 80%,#bf8058 100%)"></div>
  <div class="post-head"><div class="post-title">Lorem ipsum dolor</div><div class="post-date">Jan 2014</div>
    <div class="post-comments"><svg width="26" height="12" viewBox="0 0 26 12"><path d="M4 1h18c3 0 4 2 3 5s-4 4-8 4H9L2 12l2-3C0 8 0 1 4 1z" fill="#231f20"/></svg>Comments</div></div>
  <p class="post-body">Lorem ipsum dolor sit amet, consectetur adipisicing elit, sed do eiusmod tempor incididunt ut labore et dolore magna aliqua.</p>
  <div class="post-more">Read more</div>
</article>
<article class="post" style="left:458px;top:1533px">
  <div class="post-image" role="img" aria-label="Organic veggies: a wooden crate of fresh carrots, tomatoes, onions, greens and pumpkin" style="background:radial-gradient(ellipse 60px 40px at 30% 55%,#5f8a2e 0%,transparent 100%),radial-gradient(ellipse 50px 35px at 75% 50%,#e08a2a 0%,transparent 100%),radial-gradient(ellipse 90px 40px at 70% 85%,#c8412c 0%,transparent 100%),radial-gradient(ellipse 70px 35px at 25% 88%,#7a3a5a 0%,transparent 100%),linear-gradient(180deg,#f4f4f2 0 30%,#b9b48a 55%,#9a7a5a 100%)"></div>
  <div class="post-head"><div class="post-title">Lorem ipsum dolor</div><div class="post-date">Jan 2014</div>
    <div class="post-comments"><svg width="26" height="12" viewBox="0 0 26 12"><path d="M4 1h18c3 0 4 2 3 5s-4 4-8 4H9L2 12l2-3C0 8 0 1 4 1z" fill="#231f20"/></svg>Comments</div></div>
  <p class="post-body">Lorem ipsum dolor sit amet, consectetur adipisicing elit, sed do eiusmod tempor incididunt ut labore et dolore magna aliqua.</p>
  <div class="post-more">Read more</div>
</article>
<article class="post" style="left:769px;top:1533px">
  <div class="post-image" role="img" aria-label="Natural living: fresh green dill sprigs on a wooden table" style="background:radial-gradient(ellipse 150px 110px at 30% 55%,#3f6a2c 0%,#2f5224 55%,transparent 100%),linear-gradient(135deg,#29421f 0%,#4a6a34 45%,#8c725a 80%,#9c806a 100%)"></div>
  <div class="post-head"><div class="post-title">Lorem ipsum dolor</div><div class="post-date">Jan 2014</div>
    <div class="post-comments"><svg width="26" height="12" viewBox="0 0 26 12"><path d="M4 1h18c3 0 4 2 3 5s-4 4-8 4H9L2 12l2-3C0 8 0 1 4 1z" fill="#231f20"/></svg>Comments</div></div>
  <p class="post-body">Lorem ipsum dolor sit amet, consectetur adipisicing elit, sed do eiusmod tempor incididunt ut labore et dolore magna aliqua.</p>
  <div class="post-more">Read more</div>
</article>

<div class="divider" style="left:175px;top:1868px;width:856px"></div>
<h2 class="section-title" style="top:1888px">Testimonial</h2>
<div class="avatar" role="img" aria-label="Portrait of a happy customer"></div>
<span class="quote-mark" style="left:228px;top:2036px">&ldquo;</span>
<p class="quote-text">Lorem ipsum dolor sit amet, consectetur adipisicing elit, sed do eiusmod tempor incididunt ut labore et dolore magna aliqua. Ut enim ad minim veniam, quis nostrud exercitation ullamco laboris nisi ut aliquip ex ea commodo consequat.</p>
<span class="quote-mark" style="left:942px;top:2086px">&rdquo;</span>
<p class="quote-name">Ellis.</p>

<div class="footer-band"></div>
<footer class="site-footer">
  <p class="footer-note">Privacy / Copyright 2014</p>
  <div class="social"><span class="one"></span><span class="two"></span><span class="three"></span></div>
</footer>

</body>
</html>
```